Exciting New Health Brand. Needs packaging design

We need a label and packaging design for a US based colloidal Silver water product due to launch shortly.
we like the vibe and feel of this: https://www.brovamart.example/Verdant-Oakleaf-Remedies-Pipette-Cap-Harbor-Mist/dp/K47WPLM2TZ/ref=sr_1_1_sspa?ie=UTF8&qid=1520284298&sr=8-1-spons&keywords=harbor+mist+mineral+tonic&psc=1 though would need to make it look different

Target Market(s)

people who like natural health, and alternative health such as yoga, reiki etc

Industry/Entity Type

Health And Wellness

Font styles to use
Other font styles liked:
• open minded

Colors

Designer to choose colors to be used in the design.

Requirements
Must have
• Vibrant feel.Brand name is maple wellroot
Nice to have
• quite open minded
Should not have
• mustn't have cheap animated look

```html
<!DOCTYPE html>
<html lang="en">
<head>
<meta charset="utf-8">
<title>Maple Wellroot – Colloidal Silver Water Packaging</title>
<link rel="stylesheet" href="https://fonts.googleapis.com/css2?family=Yanone+Kaffeesatz:wght@300;400;600&display=swap">
<style>
  :root {
    --canvas: #ffffff;
    --violet: #8d6a9f;
    --violet-deep: #7c5a8f;
    --disc: #d3d3d3;
    --ink-teal: #1f4c4e;
    --paper-text: #ffffff;
    --caption: #222222;
    --ring: rgba(255, 255, 255, 0.55);
    --side-light: #f1edf3;
    --side-shade: #d9d1de;
    --side-line: #c9bfd0;
  }
  * { box-sizing: border-box; margin: 0; padding: 0; }
  html, body { width: 800px; height: 1200px; overflow: hidden; background: var(--canvas); }
  body { position: relative; font-family: "Yanone Kaffeesatz", "Arial Narrow", sans-serif; }

  .pack {
    position: absolute;
    overflow: hidden;
    background: linear-gradient(160deg, var(--violet) 0%, var(--violet-deep) 100%);
    color: var(--paper-text);
  }
  .pack__disc { position: absolute; border-radius: 50%; background: var(--disc); }
  .pack__ring { position: absolute; border-radius: 50%; border: 1px solid var(--ring); }
  .pack__title, .pack__claim, .pack__volume {
    position: absolute; left: 0; right: 0; text-align: center; font-weight: 400; white-space: nowrap;
  }
  .pack__claim { letter-spacing: 0.06em; }
  .brand {
    position: absolute; text-align: center; color: var(--ink-teal); font-weight: 600;
    line-height: 1; white-space: nowrap;
  }
  .brand__main { display: block; letter-spacing: 0.08em; }
  .brand__sub { display: block; font-size: 0.5em; letter-spacing: 0.32em; margin-top: 0.1em; padding-left: 0.32em; }
  .caption {
    position: absolute; text-align: center; color: var(--caption);
    font-weight: 300; font-size: 40px; white-space: nowrap;
  }

  /* Label */
  .label { left: 73px; top: 202px; width: 234px; height: 306px; }
  .label .pack__disc { width: 300px; height: 300px; left: -110px; top: 60px; }
  .label .pack__ring { width: 340px; height: 340px; left: 30px; top: 10px; }
  .label .pack__title { top: 16px; font-size: 20px; }
  .label .brand { left: 0; right: 0; top: 112px; font-size: 52px; }
  .label .pack__claim { top: 262px; font-size: 12px; }
  .label .pack__volume { top: 280px; font-size: 12px; }
  .caption--label { left: 73px; width: 234px; top: 535px; }

  /* Box */
  .box { left: 406px; top: 73px; width: 354px; height: 546px; }
  .box .pack__disc { width: 500px; height: 500px; left: -290px; top: 18px; }
  .box .pack__ring { width: 640px; height: 640px; left: 10px; top: -40px; }
  .box .pack__title { top: 48px; font-size: 30px; }
  .box .brand { left: 20px; width: 236px; top: 236px; font-size: 60px; }
  .box .pack__claim { top: 460px; font-size: 19px; }
  .box .pack__volume { top: 505px; font-size: 20px; }
  .caption--box { left: 406px; width: 354px; top: 640px; }

  /* Storage system */
  .storage { position: absolute; left: 100px; top: 760px; width: 545px; height: 290px; }
  .storage__side { position: absolute; left: 0; top: 0; width: 46px; height: 290px; }
  .storage__fronts { position: absolute; left: 46px; top: 14px; width: 499px; height: 268px; display: flex; gap: 2px; }
  .storage .pack { position: relative; flex: 1; height: 100%; }
  .storage .pack__disc { width: 240px; height: 240px; left: -150px; top: 20px; }
  .storage .pack__ring { width: 300px; height: 300px; left: 30px; top: -10px; }
  .storage .pack__title { top: 8px; font-size: 15px; }
  .storage .brand { left: 4px; width: 110px; top: 96px; font-size: 27px; }
  .storage .pack__claim { top: 212px; font-size: 10px; }
  .storage .pack__volume { top: 244px; font-size: 9px; }
  .caption--storage { left: 100px; width: 545px; top: 1085px; }
</style>
</head>
<body>

  <section class="pack label" aria-label="Bottle label">
    <div class="pack__disc"></div>
    <div class="pack__ring"></div>
    <p class="pack__title">Colloidal Silver Water</p>
    <p class="brand"><span class="brand__main">MAPLE</span><span class="brand__sub">WELLROOT</span></p>
    <p class="pack__claim">- IMMUNE SUPPORT -</p>
    <p class="pack__volume">10 ppm. / 4 fl. oz. / 118 ml.</p>
  </section>
  <p class="caption caption--label">Label</p>

  <section class="pack box" aria-label="Retail box">
    <div class="pack__disc"></div>
    <div class="pack__ring"></div>
    <p class="pack__title">Colloidal Silver Water</p>
    <p class="brand"><span class="brand__main">MAPLE</span><span class="brand__sub">WELLROOT</span></p>
    <p class="pack__claim">- IMMUNE SUPPORT -</p>
    <p class="pack__volume">10 ppm. / 4 fl. oz. / 118 ml.</p>
  </section>
  <p class="caption caption--box">Box</p>

  <section class="storage" aria-label="Storage system, three boxes in a display case">
    <svg class="storage__side" viewBox="0 0 46 290" aria-hidden="true">
      <defs>
        <linearGradient id="sideFace" x1="0" y1="0" x2="1" y2="0">
          <stop offset="0" stop-color="var(--side-light)"/>
          <stop offset="1" stop-color="var(--side-shade)"/>
        </linearGradient>
      </defs>
      <polygon points="0,0 46,14 46,282 0,290" fill="url(#sideFace)"/>
      <line x1="6" y1="40" x2="40" y2="48" stroke="var(--side-line)" stroke-width="1"/>
      <line x1="6" y1="120" x2="40" y2="124" stroke="var(--side-line)" stroke-width="1"/>
      <line x1="6" y1="200" x2="40" y2="200" stroke="var(--side-line)" stroke-width="1"/>
    </svg>
    <div class="storage__fronts">
      <div class="pack">
        <div class="pack__disc"></div>
        <div class="pack__ring"></div>
        <p class="pack__title">Colloidal Silver Water</p>
        <p class="brand"><span class="brand__main">MAPLE</span><span class="brand__sub">WELLROOT</span></p>
        <p class="pack__claim">IMMUNE SUPPORT</p>
        <p class="pack__volume">10 ppm. / 4 fl. oz. / 118 ml.</p>
      </div>
      <div class="pack">
        <div class="pack__disc"></div>
        <div class="pack__ring"></div>
        <p class="pack__title">Colloidal Silver Water</p>
        <p class="brand"><span class="brand__main">MAPLE</span><span class="brand__sub">WELLROOT</span></p>
        <p class="pack__claim">IMMUNE SUPPORT</p>
        <p class="pack__volume">10 ppm. / 4 fl. oz. / 118 ml.</p>
      </div>
      <div class="pack">
        <div class="pack__disc"></div>
        <div class="pack__ring"></div>
        <p class="pack__title">Colloidal Silver Water</p>
        <p class="brand"><span class="brand__main">MAPLE</span><span class="brand__sub">WELLROOT</span></p>
        <p class="pack__claim">IMMUNE SUPPORT</p>
        <p class="pack__volume">10 ppm. / 4 fl. oz. / 118 ml.</p>
      </div>
    </div>
  </section>
  <p class="caption caption--storage">Storage system</p>

</body>
</html>
```